Brochure/flyer for our trip to Paris

Our company is taking us all on a summer trip to Paris. We have some key information that we need to tell everybody about the trip. We think a nicely designed brochure or flyer, which uses our brand colours and guidelines, would be something nice to keep during the trip and as a memento afterwards.

We are looking for a brochure or a flyer which contains all the info in the attached document.

This needs to happen really fast as we actually go to Paris on the 13th August. We also need time to print it!

We can provide a library of icons. All images in the document can be changed. you don't have to use the images in the document.

Target Market(s)

People in our company. They are fun and as this is for a party the flyer needs to feel uplifting.

Industry/Entity Type

Health

Font styles to use
Other font styles liked:
• Nexa - please see attached font.

Requirements
Must have
• Designers must stick to our brand guideline, font and the colours we use.
• Please also see attached content for the flyer.
• This website shows our style - https://www.kelotrix.com/fr
Should not have
• Please don't make it too tacky or too much about French things. It can be a bit playful but not too much.

```html
<!DOCTYPE html>
<html lang="en">
<head>
<meta charset="utf-8">
<title>Translations – Paris Trip</title>
<link href="https://fonts.googleapis.com/css2?family=Lexend:wght@600&family=Questrial&display=swap" rel="stylesheet">
<style>
  :root {
    --brand-orange: #eb5a2a;
    --brand-navy: #3b4f9a;
    --brand-teal: #6bc3c5;
    --brand-blue: #4285c6;
    --text-light: #fdf2ec;
  }
  html, body {
    margin: 0;
    padding: 0;
    width: 779px;
    height: 1200px;
    overflow: hidden;
    background: var(--brand-orange);
  }
  .page {
    position: relative;
    width: 779px;
    height: 1200px;
    background: var(--brand-orange);
    color: var(--text-light);
    font-family: "Questrial", "Helvetica Neue", Arial, sans-serif;
  }
  .side-stripes {
    position: absolute;
    top: 0;
    right: 0;
    width: 68px;
    height: 1200px;
  }
  .page-title {
    position: absolute;
    left: 56px;
    top: 40px;
    margin: 0;
    font-family: "Lexend", "Helvetica Neue", Arial, sans-serif;
    font-weight: 600;
    font-size: 51px;
    letter-spacing: 0.2px;
    line-height: 1;
  }
  .phrase-list {
    position: absolute;
    left: 57px;
    top: 130px;
    margin: 0;
    padding: 0;
    list-style: none;
    display: flex;
    flex-direction: column;
    gap: 28.4px;
    font-size: 22px;
    line-height: 28.2px;
    white-space: nowrap;
  }
  .phrase-list li { margin: 0; }
</style>
</head>
<body>
  <main class="page">
    <svg class="side-stripes" viewBox="0 0 68 1200" aria-hidden="true">
      <rect x="0" y="0" width="68" height="301" fill="var(--brand-navy)"/>
      <rect x="0" y="301" width="68" height="301" fill="var(--brand-teal)"/>
      <rect x="0" y="602" width="68" height="301" fill="var(--brand-orange)"/>
      <rect x="0" y="903" width="68" height="297" fill="var(--brand-blue)"/>
    </svg>

    <h1 class="page-title">Translations</h1>

    <ul class="phrase-list">
      <li class="intro">Some Must-know French Phrases for Savvy<br>Travellers:</li>
      <li>Bonjour. (Hello)</li>
      <li>Oui / Non (Yes / No)</li>
      <li>Parlezvous anglais ? (Do you speak English?)</li>
      <li>Où est le métro? (Where is the Metro?)</li>
      <li>Où est…? (Where is…?)</li>
      <li>Où est le guichet ? (Where is the ticket window?)</li>
      <li>Combien ça coûte? (How much does it cost?)</li>
      <li>Merci! (Thank you!)</li>
      <li>Bonsoir (Hello/good evening)</li>
      <li>Au Revoir (Goodbye)</li>
      <li>Puisje me connecter à Internet? (Can I get on the<br>internet?)</li>
      <li>Je ne comprends pas. (I don’t understand)</li>
      <li>Je ne sais pas. (I don’t know)</li>
      <li>&nbsp;Estce que vous pouvez l'écrire? (Could you please<br>write it down?)</li>
      <li>Pouvezvous m’aider, s’il vous plaît? (Can you help me<br>please?)</li>
    </ul>
  </main>
</body>
</html>
```